Financial investment calculator report for real estae - layout & design

I am looking to Create a web report utilizing the attached information. It is an investment calculator report that will be customized report based on an online calculator. Therefore the report will need to be designed in a manner that a backend developer will be able to build off of.

The report will need to be web based but also printed in PDF format. The report will need to include the calculation format as well as be templeted to add a report user unique profile information like Headshot, Business Logo, Name, Telephone number, email etc.

The report should be modern and clean and easy to read and use a modern clean template design. It should be able to be easily color customized by the end user to produce templets in Red, Blue, Green, and Greyscale.

The report should be no more than 3 pages total with out breaking up the sections.

Section One - Cover sheet including agent bio info, Report Title and property address (both prominent), 400 Character space for property description, Property Pictures (3), and a velmo Trails integration image showing property location, It should also have room for about 100 words for a text disclaimer. (I will provide text soon)

Section Two - Inputs from the calculator

Section 3 - The Four Benefits & Rates of Return

Once I have a completed/approved form I will have about a half dozen forms/reports that will need to be laid out with a similar aesthetic.

Feel free to ask me any questions. Thank You
Tobin

This report will be produced by real estate agents forvtheir investor clients. It should denote professionalism

Sans Serif

0054AA
0677BA
7BADD7
CADEEF
E8F1F8
00AB8E
00BBA5
67D7C9
C6EFE9
E9F9F6
EB3D1F
EC4F4E
F09395
F8D3D4
FCEDEE

```html
<!DOCTYPE html>
<html lang="en">
<head>
<meta charset="utf-8">
<title>Investment Analysis – 412 Ashgrove</title>
<link href="https://fonts.googleapis.com/css2?family=Rubik:wght@500;600&family=Inter:wght@400;500;600&display=swap" rel="stylesheet">
<style>
  :root{
    --brand:#A11C23;
    --brand-text:#A3191F;
    --ink:#333333;
    --ink-soft:#555555;
    --label:#6b6b6b;
    --card:#F2F2F2;
    --white:#ffffff;
    --disclaimer-head:#E9B9B6;
    --disclaimer-text:#F3D59A;
    --frame:#F1D6D8;
  }
  *{box-sizing:border-box;margin:0;padding:0}
  html,body{width:927px;height:1200px;overflow:hidden;background:var(--white)}
  body{font-family:"Inter",Arial,sans-serif;color:var(--ink);position:relative}

  .top-band{position:absolute;left:0;top:0;width:927px;height:205px;background:var(--brand)}
  .print-meta{position:absolute;top:8px;left:12px;right:12px;display:flex;justify-content:space-between;
    font-size:10px;color:rgba(255,255,255,.35)}

  .brand{position:absolute;left:78px;top:68px;display:flex;align-items:center;gap:14px}
  .brand-mark{width:74px;height:74px;border:3px solid var(--white);border-radius:50%}
  .brand-name{font-family:"Rubik",Arial,sans-serif;font-weight:500;color:var(--white);line-height:1}
  .brand-name .primary{display:block;font-size:40px;letter-spacing:2px}
  .brand-name .secondary{display:block;font-size:14px;letter-spacing:1px;margin-top:4px;text-align:center}

  .agent-card{position:absolute;left:614px;top:88px;width:235px;height:352px;background:var(--card);
    border-radius:12px;text-align:center}
  .agent-photo{width:146px;height:146px;margin:26px auto 0;border-radius:50%;border:2px solid var(--brand);
    padding:5px;background:var(--white)}
  .agent-photo div{width:100%;height:100%;border-radius:50%;
    background:radial-gradient(circle at 50% 40%,#c9a58c 0%,#8d6e5e 45%,#2c3550 100%)}
  .agent-role{margin-top:26px;font-size:11px;font-weight:600;letter-spacing:3px;color:var(--brand-text)}
  .agent-name{margin-top:12px;font-size:16px;font-weight:600;color:var(--ink)}
  .agent-line{font-size:16px;color:var(--ink);line-height:23px}

  .report-title{position:absolute;left:90px;top:258px;font-family:"Rubik",Arial,sans-serif;font-weight:600;
    font-size:46px;line-height:54px;color:var(--ink)}
  .report-title .address{display:block;color:var(--brand-text)}
  .report-subtitle{position:absolute;left:90px;top:360px;font-size:21px;color:var(--brand-text)}

  .section-label{font-size:12px;font-weight:600;letter-spacing:3px;color:var(--label)}
  .about{position:absolute;left:90px;top:440px;width:470px}
  .about p{margin-top:14px;font-size:15px;line-height:21px;color:var(--ink)}

  .photo{position:absolute;top:573px;height:218px;border-radius:14px;border:2px solid var(--frame);padding:5px;background:var(--white)}
  .photo div{width:100%;height:100%;border-radius:10px}
  .photo-exterior{left:74px;width:246px}
  .photo-exterior div{background:linear-gradient(180deg,#5d6f9e 0%,#8f8fb0 45%,#6e6a62 70%,#3d4a2e 100%)}
  .photo-hall{left:342px;width:241px}
  .photo-hall div{background:linear-gradient(180deg,#e9e4dc 0%,#1f5f86 30%,#1b4f73 70%,#b8a48e 100%)}
  .photo-lounge{left:606px;width:246px}
  .photo-lounge div{background:linear-gradient(180deg,#f3f1ee 0%,#d9d7d2 55%,#a9aaa8 100%)}

  .location-map{position:absolute;left:74px;top:821px;width:778px;height:185px;border-radius:16px;
    border:2px solid var(--frame);padding:4px;background:var(--white)}
  .location-map div{width:100%;height:100%;border-radius:12px;
    background:linear-gradient(160deg,#f4f5f4 0%,#eceeec 50%,#e6ece6 100%)}

  .disclaimer-band{position:absolute;left:0;top:1030px;width:927px;height:147px;background:var(--brand);padding:20px 90px 0}
  .disclaimer-band h2{font-size:12px;font-weight:600;letter-spacing:3px;color:var(--disclaimer-head)}
  .disclaimer-band p{margin-top:18px;font-size:14.5px;line-height:22px;color:var(--disclaimer-text)}

  .page-footer{position:absolute;left:12px;right:40px;top:1180px;display:flex;justify-content:space-between;
    font-size:10px;color:#222}
</style>
</head>
<body>
  <header class="top-band">
    <div class="print-meta"><span>05/09/20 9:50 PM</span><span>Investment Analysis</span></div>
    <div class="brand">
      <div class="brand-mark"></div>
      <div class="brand-name"><span class="primary">MERIDIAN</span><span class="secondary">REALTY</span></div>
    </div>
  </header>

  <aside class="agent-card">
    <div class="agent-photo"><div role="img" aria-label="Agent headshot"></div></div>
    <div class="agent-role">AGENT</div>
    <div class="agent-name">Darren Hollis</div>
    <div class="agent-line">admin1</div>
    <div class="agent-line">(555) 204-7719</div>
    <div class="agent-line">darren@meridianmail.test</div>
  </aside>

  <h1 class="report-title">Investment Analysis<span class="address">412 Ashgrove</span></h1>
  <div class="report-subtitle">15-Plex of 1bd/1bth Apartments</div>

  <section class="about">
    <div class="section-label">ABOUT THE PROPERTY</div>
    <p>Lorem ipsum is a placeholder text commonly used to demonstrate the visual form of a document or a typeface without relying on meaningful content.</p>
  </section>

  <figure class="photo photo-exterior"><div role="img" aria-label="Exterior photo of the property at dusk"></div></figure>
  <figure class="photo photo-hall"><div role="img" aria-label="Interior photo of a hallway with artwork and a dresser"></div></figure>
  <figure class="photo photo-lounge"><div role="img" aria-label="Interior photo of a living room with a sofa"></div></figure>

  <figure class="location-map"><div role="img" aria-label="Map showing the property location"></div></figure>

  <section class="disclaimer-band">
    <h2>DISCLAIMER</h2>
    <p>In publishing and graphic design, Lorem ipsum is a placeholder text commonly used to demonstrate the visual form of a document or a typeface without relying on meaningful content. Lorem ipsum may be used as a placeholder before final copy is available.</p>
  </section>

  <footer class="page-footer"><span>https://www.reportdesk.example/report/pdf/5</span><span>1/3</span></footer>
</body>
</html>
```